Visitenkarten/Briefpaier/Kassenkassenbelege für Juwelier
Zielgruppe
Mittelständischer Juwelier mit zwei Filialen. Klassischer Schmuck, Uhren und Modeschmuck
Aufgabenstellung
Es müssen für zwei Geschäfte Visitenkarten, Briefpapier (A4) und Kassenkassenbelege (A6) erstellt werden. Logo und fenwiro im Anhang. Ein Farbkonzept besteht noch nicht. Die Idee geht in Richtung Bordeaux-Rot.
Generell:
(1) Sieht erstmal nach viel Beschreibung aus, bitte nicht entmutigen lassen, sind zu 90% nur austauschbare Inhalts-/Kontaktdaten.
(2) Für meine Zwecke reicht es vollkommen aus, wenn bei den Vorschlägen zur Arbeitsersparnis erstmal nur mit einer Adresse gearbeitet wird. Wenn ich dann den zutreffenden Designvorschlag gefunden habe, können wir die zweite Adresse in dem ersten Format umsetzen. Ich denke das spart Zeit und Nerven.
(3) Bitte Angaben wie "Tel.:" oder "USt.- ID:" nicht wörtlich nehmen, es soll dabei klar sein worum es geht; wenn "Telefon" ausgeschrieben besser aussieht, bitte in der optisch ansprechenderen Form verwenden.
(4) Bei Fragen, bitte fragen!
(5) Viel Spass bei dem Projekt - Ich freu' mich auf die Vorschläge!
Visitenkarten(1):
Juwelier Brandauer GmbH
www.juwelier-brandauer-example.de
Visitenkarten(2):
Visitenkarten(generell):
(1) Die einzelnen Daten können durch Hervorhebungen wie Adresse, Kontakt, Online/Internet unterteilt bzw. hervorgehoben werden.
(2) Die Visitenkarten sollen farbig gedruckt werden; geplant ist weiß als Hintergrund ist aber nicht zwingend bei einer guten anderen Idee
Briefpapier:
(1)Absender im Adressfeld für DIN-lang Briefumschläge mit Fenster:
(2)Informationen im Footer/Seitenbereich:
Juwelier Brandauer Gmb..

```html
<!DOCTYPE html>
<html lang="de">
<head>
<meta charset="utf-8">
<title>Briefpapier Brandauer</title>
<link href="https://fonts.googleapis.com/css2?family=Source+Sans+3:wght@400;600;700&display=swap" rel="stylesheet">
<style>
  :root {
    --paper: #ffffff;
    --canvas: #ffffff;
    --taupe: #857a70;
    --taupe-text: #7d7168;
    --slate: #666666;
    --mark: #555555;
    --body-text: #777777;
    --sidebar-text: #f4f1ee;
  }
  * { margin: 0; padding: 0; box-sizing: border-box; }
  html, body { width: 1200px; height: 814px; overflow: hidden; background: var(--canvas); }
  body { position: relative; font-family: "Source Sans 3", sans-serif; }

  .crop { position: absolute; background: var(--mark); }
  .crop.v { width: 1px; height: 30px; }
  .crop.h { height: 1px; width: 30px; }

  .sheet {
    position: absolute; top: 50px; width: 503px; height: 711px;
    background: var(--paper);
    box-shadow: 2px 3px 5px rgba(0,0,0,0.28);
    overflow: hidden;
  }
  .sheet--sidebar { left: 50px; }
  .sheet--line { left: 646px; }

  .fold { position: absolute; left: 0; width: 17px; height: 1px; background: #bbb; }

  .window-corner { position: absolute; width: 11px; height: 11px; border-color: var(--mark); border-style: solid; border-width: 0; }
  .tl { border-top-width: 1px; border-left-width: 1px; }
  .tr { border-top-width: 1px; border-right-width: 1px; }
  .bl { border-bottom-width: 1px; border-left-width: 1px; }
  .br { border-bottom-width: 1px; border-right-width: 1px; }

  .wordmark {
    position: absolute; display: flex; align-items: center; gap: 8px;
    font-weight: 400; color: var(--taupe-text); white-space: nowrap; line-height: 1;
  }
  .wordmark .dot { display: block; width: 10px; height: 10px; background: var(--taupe-text); }

  .sidebar { position: absolute; top: 0; right: 0; width: 135px; height: 100%; background: var(--taupe); }

  .contact { position: absolute; top: 43px; font-size: 6.9px; line-height: 10px; }
  .contact .company { font-size: 8.6px; font-weight: 600; line-height: 11px; margin-bottom: 1px; }
  .contact .block { margin-top: 10px; }
  .contact .fine { font-size: 5.6px; line-height: 7.7px; }
  .contact .fine.first { margin-top: 14px; }
  .contact .fine.gap { margin-top: 10px; }
  .contact .branch { font-size: 6.6px; line-height: 7.7px; margin-top: 12px; }

  .sheet--sidebar .contact { left: 380px; color: var(--sidebar-text); }
  .sheet--line .contact { left: 378px; color: var(--body-text); }
  .sheet--line .contact .company { color: var(--mark); }

  .divider { position: absolute; left: 368px; top: 0; width: 1px; height: 242px; background: var(--slate); }
  .foot-band { position: absolute; left: 0; bottom: 0; width: 100%; height: 6px; background: var(--taupe); }
</style>
</head>
<body>
  <span class="crop v" style="left:50px;top:5px"></span>
  <span class="crop v" style="left:553px;top:5px"></span>
  <span class="crop v" style="left:646px;top:5px"></span>
  <span class="crop v" style="left:1148px;top:5px"></span>
  <span class="crop v" style="left:50px;top:777px"></span>
  <span class="crop v" style="left:553px;top:777px"></span>
  <span class="crop v" style="left:646px;top:777px"></span>
  <span class="crop v" style="left:1148px;top:777px"></span>
  <span class="crop h" style="left:5px;top:50px"></span>
  <span class="crop h" style="left:568px;top:50px"></span>
  <span class="crop h" style="left:601px;top:50px"></span>
  <span class="crop h" style="left:1164px;top:50px"></span>
  <span class="crop h" style="left:5px;top:761px"></span>
  <span class="crop h" style="left:568px;top:761px"></span>
  <span class="crop h" style="left:601px;top:761px"></span>
  <span class="crop h" style="left:1164px;top:761px"></span>

  <!-- Variant A: taupe sidebar -->
  <section class="sheet sheet--sidebar">
    <div class="wordmark" style="left:82px;top:76px;font-size:20px"><span class="dot"></span>Brandauer</div>

    <span class="window-corner tl" style="left:24px;top:122px"></span>
    <span class="window-corner tr" style="left:228px;top:122px"></span>
    <span class="window-corner bl" style="left:24px;top:195px"></span>
    <span class="window-corner br" style="left:228px;top:195px"></span>

    <span class="fold" style="top:253px"></span>
    <span class="fold" style="top:491px"></span>

    <aside class="sidebar"></aside>
    <div class="contact">
      <p class="company">Juwelier Brandauer GmbH</p>
      <p>Lindenweg 14</p>
      <p>45127 Musterstadt</p>
      <div class="block">
        <p>Tel.: 0201-555010</p>
        <p>Fax: 0201-555011</p>
        <p>info@juwelier-brandauer-example.de</p>
        <p>www.juwelier-brandauer-example.de</p>
      </div>
      <p class="fine first">Bankverbindung:<br>Musterbank AG<br>IBAN: DE00 1234 5678 0000 1111 22<br>BIC: MUSTDEXX</p>
      <p class="fine gap">Steuernummer:<br>000/1234/5678<br>USt.- ID: DE 000111222</p>
      <p class="branch">Filiale:<br>Ahornallee 8<br>45999 Beispielstadt</p>
    </div>
  </section>

  <!-- Variant B: hairline divider -->
  <section class="sheet sheet--line">
    <div class="wordmark" style="left:40px;top:52px;font-size:24px"><span class="dot"></span>Brandauer</div>

    <span class="window-corner tl" style="left:23px;top:122px"></span>
    <span class="window-corner tr" style="left:228px;top:122px"></span>
    <span class="window-corner bl" style="left:23px;top:195px"></span>
    <span class="window-corner br" style="left:228px;top:195px"></span>

    <span class="fold" style="top:253px"></span>
    <span class="fold" style="top:491px"></span>

    <span class="divider"></span>
    <div class="contact">
      <p class="company">Juwelier Brandauer GmbH</p>
      <p>Lindenweg 14</p>
      <p>45127 Musterstadt</p>
      <div class="block">
        <p>Tel.: 0201-555010</p>
        <p>Fax: 0201-555011</p>
        <p>info@juwelier-brandauer-example.de</p>
        <p>www.juwelier-brandauer-example.de</p>
      </div>
      <p class="fine first">Bankverbindung:<br>Musterbank AG<br>IBAN: DE00 1234 5678 0000 1111 22<br>BIC: MUSTDEXX</p>
      <p class="fine gap">Steuernummer:<br>000/1234/5678<br>USt.- ID: DE 000111222</p>
      <p class="branch">Filiale:<br>Ahornallee 8<br>45999 Beispielstadt</p>
    </div>
    <span class="foot-band"></span>
  </section>
</body>
</html>
```